Brightwave Reach - Business Card

We need a business card for a Social Media Marketing company that specializes in online marketing for small businesses in Canada using common Social Media platforms such as Pictora, Kinloop, Blinkit & Chirpo.

I have uploaded a copy of our logo which I would like utilized in the business card. We would like the business card to be modern yet classy design.

Our website is www.brightwavereach.ca

Industry/Entity Type

Marketing

Contact Information for Business Card

Email: info@brightwavereach.ca
Website: www.brightwavereach.ca
Telephone: 604-392-5108

Colors

Designer to choose colors to be used in the design.

Requirements
Must have
• Social Media icons on reverse
• Please add some designs with color.

```html
<!DOCTYPE html>
<html lang="en">
<head>
<meta charset="utf-8">
<title>Brightwave Reach – Business Card</title>
<link href="https://fonts.googleapis.com/css2?family=Montserrat:wght@400;600;700;800&display=swap" rel="stylesheet">
<style>
  :root {
    --page: #ffffff;
    --card-light: #e8e5e3;
    --accent: #cc604b;
    --charcoal: #55504c;
    --ink: #2a2624;
    --mark: #4a4542;
    --faint: #736e6a;
    --white: #ffffff;
  }
  * { margin: 0; padding: 0; box-sizing: border-box; }
  html, body {
    width: 1200px; height: 1200px; overflow: hidden;
    background: var(--page);
    font-family: "Montserrat", sans-serif;
  }
  .canvas { position: relative; width: 1200px; height: 1200px; }

  .card { position: absolute; left: 157px; width: 838px; overflow: hidden; }

  /* Front */
  .card--front { top: 78px; height: 480px; background: var(--card-light); }
  .holder { position: absolute; left: 69px; top: 193px; color: var(--ink); }
  .holder__name { font-weight: 600; font-size: 21px; line-height: 1.25; }
  .holder__title { font-weight: 400; font-size: 21px; line-height: 1.3; letter-spacing: 0.3px; }

  .wordmark {
    position: absolute; right: 44px; top: 92px;
    display: flex; align-items: center; gap: 16px;
  }
  .wordmark__square { width: 22px; height: 22px; background: var(--mark); }
  .wordmark__name {
    font-weight: 800; font-size: 40px; line-height: 1.05;
    color: var(--mark); text-transform: uppercase; text-align: right;
  }

  .contact-band {
    position: absolute; left: 0; top: 289px; width: 100%; height: 191px;
    background: var(--accent);
  }
  .contact-list { list-style: none; position: absolute; left: 63px; top: 23px; }
  .contact-item {
    display: flex; align-items: center; height: 50px;
    color: var(--white); font-size: 22px; font-weight: 400; letter-spacing: 0.4px;
  }
  .contact-item svg { width: 40px; height: 40px; margin-right: 24px; flex: none; }

  /* Back */
  .card--back { top: 632px; height: 475px; background: var(--charcoal); }
  .backdrop-name {
    position: absolute; left: -12px; top: 110px;
    transform: rotate(-4deg); transform-origin: left top;
    font-weight: 800; font-size: 104px; line-height: 0.95;
    color: var(--faint); text-transform: uppercase;
  }
  .social-list {
    list-style: none; position: absolute; left: 590px; top: 60px; width: 228px;
    text-align: center; color: var(--white);
  }
  .social-item { height: 130px; display: flex; flex-direction: column; align-items: center; }
  .social-item:last-child { margin-top: 10px; }
  .social-item__platform {
    display: flex; align-items: center; gap: 8px; height: 54px;
    font-weight: 600; font-size: 17px; letter-spacing: 0.5px;
  }
  .social-item__dot { width: 12px; height: 12px; border-radius: 50%; background: var(--white); }
  .social-item__handle { font-weight: 600; font-size: 21px; margin-top: 14px; }
</style>
</head>
<body>
<div class="canvas">

  <section class="card card--front" aria-label="Card front">
    <div class="holder">
      <p class="holder__name">Your Name</p>
      <p class="holder__title">Managing Director</p>
    </div>

    <div class="wordmark">
      <span class="wordmark__square"></span>
      <span class="wordmark__name">Brightwave<br>Reach</span>
    </div>

    <div class="contact-band">
      <ul class="contact-list">
        <li class="contact-item">
          <svg viewBox="0 0 40 40" fill="none" stroke="#fff" stroke-width="2">
            <rect x="3" y="9" width="34" height="22" rx="2"/>
            <path d="M3 10 L20 23 L37 10"/>
          </svg>
          info@brightwavereach.ca
        </li>
        <li class="contact-item">
          <svg viewBox="0 0 40 40" fill="none" stroke="#fff" stroke-width="2">
            <circle cx="20" cy="20" r="17"/>
            <ellipse cx="20" cy="20" rx="7" ry="17"/>
            <path d="M3 20 H37 M6 12 H34 M6 28 H34"/>
          </svg>
          www.brightwavereach.ca
        </li>
        <li class="contact-item">
          <svg viewBox="0 0 40 40" fill="none" stroke="#fff" stroke-width="2" stroke-linejoin="round">
            <path d="M11 4 L17 12 L13 17 C15 22 18 25 23 27 L28 23 L36 29 L32 36 C18 35 5 22 4 8 Z"/>
          </svg>
          604-392-5108
        </li>
      </ul>
    </div>
  </section>

  <section class="card card--back" aria-label="Card back">
    <div class="backdrop-name" aria-hidden="true">Brightwave<br>Reach</div>

    <ul class="social-list">
      <li class="social-item">
        <span class="social-item__platform"><span class="social-item__dot"></span>Kinloop</span>
        <span class="social-item__handle">Brightwave Reach</span>
      </li>
      <li class="social-item">
        <span class="social-item__platform"><span class="social-item__dot"></span>Chirpo</span>
        <span class="social-item__handle">@brightwavereach</span>
      </li>
      <li class="social-item">
        <span class="social-item__platform"><span class="social-item__dot"></span>Pictora</span>
        <span class="social-item__handle">brightwavereach</span>
      </li>
    </ul>
  </section>

</div>
</body>
</html>
```